Invest in Real Estate housing and apartment development projects in Lima - Peru

Need a presentation for Grupo Venora, a top Real Estate developer from Peru who is looking for new leading investors such as Top Regional and Worldwide Real Estate funds and Regional Family offices and High Networth individuals to invest in Real Estate projects developed by/with Grupo Venora. Venora is focused on middle income apartments (housing) and has developed and delivered aprox 1400 apartments, and is currently developing and building 400 apartments. Venora currently has a potential to develop 1500 more apartments. And is looking to raise between US $50 and 60mm dollars a year in additional new investments, all focused on real estate housing (essentially vertical housing, apartments)
I have already some information and slides prepared with information regarding management fees, development and sales/marketing fees, success fees which are alligned to IRR of the project.

Target Market(s)

Real Estate investors in Latin America

Industry/Entity Type

Real Estate Development

Colors

Requirements
Must have
• Graphs and pictures of real estate projects. Data of housing market from Lima, capital of Peru compared to other top capitals in South America

```html
<!DOCTYPE html>
<html lang="en">
<head>
<meta charset="utf-8">
<title>Grupo Venora — Investor Presentation Overview</title>
<link href="https://fonts.googleapis.com/css2?family=Raleway:wght@300;400;600;700;800&display=swap" rel="stylesheet">
<style>
:root{
  --green:#6cb33f;
  --green-dark:#4f9a2c;
  --green-light:#8cc84b;
  --brown:#3e2c25;
  --brown-mid:#5a4037;
  --grey:#9b9b9b;
  --grey-light:#e6e6e6;
  --ink:#333;
  --page:#eeeeee;
  --white:#fff;
}
*{box-sizing:border-box;margin:0;padding:0}
html,body{width:894px;height:1200px;overflow:hidden;background:var(--page)}
body{font-family:"Raleway",sans-serif;color:var(--ink)}
.deck{display:grid;grid-template-columns:repeat(3,291px);grid-template-rows:repeat(7,165px);gap:6px;padding:4px;width:894px;height:1200px}
.slide{position:relative;background:var(--white);overflow:hidden;box-shadow:0 1px 2px rgba(0,0,0,.18)}
.slide svg.art{position:absolute;inset:0;width:291px;height:165px}
.slide-title{position:absolute;left:13px;top:10px;font-size:13px;font-weight:400;color:#3a3a3a;letter-spacing:.1px;z-index:2}
.slide-title::after{content:"";display:block;width:16px;height:1.5px;background:var(--green);margin-top:3px}
.slide-title.caps{text-transform:uppercase;font-weight:300;font-size:13px}
.slide-title.light{color:#fff}
.slide-title.light::after{background:#fff}
svg text{font-family:"Raleway",sans-serif}
.tiny{font-size:2.8px;fill:#9a9a9a}
.tiny-w{font-size:2.8px;fill:#fff}
.lbl{font-size:4px;fill:#444;font-weight:600}
.lbl-w{font-size:3.6px;fill:#fff;font-weight:700}
.num{font-weight:300;fill:#444}
.brand{font-weight:700;fill:var(--brown)}
</style>
</head>
<body>
<main class="deck">

<!-- 1 Property -->
<section class="slide">
  <h2 class="slide-title">Property Infographic</h2>
  <svg class="art" viewBox="0 0 291 165">
    <rect x="25" y="50" width="130" height="95" rx="6" fill="#d9d9d9" role="img" aria-label="Illustration of a key with tags for house, rent, penthouse and sale"/>
    <text x="185" y="78" font-size="5" fill="#6cb33f" font-weight="600">Description</text>
    <text x="185" y="96" font-size="16" class="num">35%</text>
    <text x="212" y="86" class="tiny">Of shopping carts are</text>
    <text x="212" y="90" class="tiny">abandoned right before</text>
    <text x="212" y="94" class="tiny">the transaction is done</text>
    <text x="185" y="104" class="tiny">For every 6 emails received, we get 3 Phone</text>
    <text x="185" y="108" class="tiny">calls. Suitable for all categories business and</text>
    <text x="185" y="112" class="tiny">personal presentation. Suitable for all</text>
    <text x="185" y="116" class="tiny">categories business and personal use.</text>
    <circle cx="8" cy="159" r="2" fill="#6cb33f"/><text x="12" y="161" font-size="5" class="brand">Venora</text>
    <text x="36" y="161" class="tiny">© Grupo Venora. All rights reserved</text>
  </svg>
</section>

<!-- 2 House -->
<section class="slide">
  <h2 class="slide-title">House Infographic</h2>
  <svg class="art" viewBox="0 0 291 165">
    <rect x="0" y="40" width="291" height="100" fill="#cfcfcf" role="img" aria-label="City skyline with green houses rising by year"/>
    <rect x="100" y="105" width="26" height="35" fill="#6cb33f"/><rect x="131" y="88" width="26" height="52" fill="#5aa532"/>
    <rect x="162" y="78" width="26" height="62" fill="#3e2c25"/><rect x="193" y="68" width="26" height="72" fill="#6cb33f"/>
    <rect x="224" y="56" width="26" height="84" fill="#5aa532"/>
    <text x="106" y="122" class="lbl-w">+20%</text><text x="137" y="105" class="lbl-w">+35%</text>
    <text x="168" y="98" class="lbl-w">+30%</text><text x="199" y="90" class="lbl-w">+40%</text><text x="230" y="80" class="lbl-w">+50%</text>
    <text x="30" y="115" font-size="4.5" fill="#333" font-weight="700">Increasing</text>
    <text x="22" y="121" class="tiny">The arrow is a graphic</text>
    <path d="M68 125v-8h-3l5-6 5 6h-3v8z" fill="#3e2c25"/>
    <rect x="0" y="140" width="291" height="25" fill="#3e2c25"/>
    <g font-size="3" fill="#fff" font-weight="700" text-anchor="middle">
      <circle cx="113" cy="140" r="5" fill="#2a1c17"/><text x="113" y="141">2011</text>
      <circle cx="144" cy="140" r="5" fill="#2a1c17"/><text x="144" y="141">2012</text>
      <circle cx="175" cy="140" r="5" fill="#2a1c17"/><text x="175" y="141">2013</text>
      <circle cx="206" cy="140" r="5" fill="#2a1c17"/><text x="206" y="141">2014</text>
      <circle cx="237" cy="140" r="5" fill="#2a1c17"/><text x="237" y="141">2015</text>
    </g>
  </svg>
</section>

<!-- 3 Construction -->
<section class="slide">
  <h2 class="slide-title">Construction Infographic</h2>
  <svg class="art" viewBox="0 0 291 165">
    <rect x="8" y="50" width="140" height="115" fill="#dedede" role="img" aria-label="Tower crane lifting a green house over a city skyline"/>
    <text x="158" y="58" font-size="4.2" fill="#333" font-weight="700">Description</text>
    <text x="158" y="63" class="tiny">For every 6 emails received, we get 3 Phone calls. Suitable for</text>
    <text x="158" y="67" class="tiny">all categories business and personal presentation. Suitable</text>
    <text x="158" y="71" class="tiny">for all categories because this is your presentation.</text>
    <line x1="168" y1="85" x2="168" y2="140" stroke="#ccc" stroke-width=".5"/>
    <line x1="168" y1="140" x2="280" y2="140" stroke="#ccc" stroke-width=".5"/>
    <rect x="180" y="98" width="5" height="42" fill="#3e2c25"/><rect x="188" y="108" width="5" height="32" fill="#6cb33f"/>
    <rect x="212" y="112" width="5" height="28" fill="#3e2c25"/><rect x="220" y="96" width="5" height="44" fill="#6cb33f"/>
    <rect x="244" y="106" width="5" height="34" fill="#3e2c25"/><rect x="252" y="102" width="5" height="38" fill="#6cb33f"/>
    <text x="181" y="145" class="tiny">Category 1</text><text x="213" y="145" class="tiny">Category 2</text><text x="245" y="145" class="tiny">Category 3</text>
  </svg>
</section>

<!-- 4 Construction 2 -->
<section class="slide">
  <h2 class="slide-title">Construction Infographic</h2>
  <svg class="art" viewBox="0 0 291 165">
    <text x="13" y="48" font-size="4" font-weight="700" fill="#333">Workers</text>
    <text x="13" y="53" class="tiny">For every 6 emails received, we get 3 Phone calls. Suitable for all</text>
    <text x="13" y="57" class="tiny">categories business and personal presentation, feel free to</text>
    <text x="13" y="61" class="tiny">write it because this is your presentation.</text>
    <g fill="#3e2c25"><circle cx="152" cy="52" r="3.2"/><circle cx="160" cy="52" r="3.2"/><circle cx="168" cy="52" r="3.2"/><circle cx="176" cy="52" r="3.2"/><circle cx="184" cy="52" r="3.2"/><circle cx="192" cy="52" r="3.2"/><circle cx="200" cy="52" r="3.2"/></g>
    <g fill="#bbb"><circle cx="208" cy="52" r="3.2"/><circle cx="216" cy="52" r="3.2"/><circle cx="224" cy="52" r="3.2"/></g>
    <text x="230" y="55" font-size="8" class="num">7/10</text>
    <text x="240" y="90" font-size="3.6" font-weight="700" fill="#333">Description</text>
    <text x="240" y="94" class="tiny">Of shipping carts are</text><text x="240" y="98" class="tiny">abandoned right before</text>
    <rect x="0" y="70" width="291" height="95" fill="#e2e2e2" role="img" aria-label="Skyline with three dump trucks carrying earth"/>
    <g text-anchor="middle">
      <text x="30" y="82" class="tiny">2016</text><text x="30" y="92" font-size="8" class="num">32,8</text>
      <text x="105" y="80" class="tiny">2017</text><text x="105" y="90" font-size="8" fill="#6cb33f" font-weight="300">27,3</text>
      <text x="170" y="80" class="tiny">2018</text><text x="170" y="90" font-size="8" fill="#6cb33f" font-weight="300">38,2</text>
      <text x="255" y="110" font-size="8" class="num">32,8</text>
    </g>
    <rect x="0" y="155" width="291" height="10" fill="#3e2c25"/>
  </svg>
</section>

<!-- 5 Apartment -->
<section class="slide">
  <h2 class="slide-title">Apartment Infographic</h2>
  <svg class="art" viewBox="0 0 291 165">
    <rect x="0" y="80" width="291" height="60" fill="#ececec"/>
    <rect x="38" y="118" width="22" height="22" fill="#3e2c25"/><rect x="93" y="112" width="22" height="28" fill="#6cb33f"/>
    <rect x="140" y="100" width="22" height="40" fill="#6cb33f"/><rect x="188" y="88" width="22" height="52" fill="#5a4037"/>
    <rect x="236" y="58" width="22" height="82" fill="#6cb33f"/>
    <g font-size="4" font-weight="700" text-anchor="middle">
      <text x="49" y="115" fill="#3e2c25">$105.00</text><text x="104" y="109" fill="#6cb33f">$122.00</text>
      <text x="151" y="97" fill="#6cb33f">$125.00</text><text x="199" y="85" fill="#3e2c25">$153.00</text>
      <text x="247" y="55" fill="#6cb33f">$255.50</text>
    </g>
    <rect x="0" y="140" width="291" height="25" fill="#3e2c25"/>
    <g class="lbl-w" text-anchor="middle">
      <text x="49" y="150">San Francisco</text><text x="104" y="150">London</text><text x="151" y="150">Tokyo</text><text x="199" y="150">New York</text><text x="247" y="150">Hongkong</text>
    </g>
  </svg>
</section>

<!-- 6 House 2 -->
<section class="slide">
  <h2 class="slide-title">House Infographic</h2>
  <svg class="art" viewBox="0 0 291 165">
    <path d="M0 115 Q80 95 150 110 T291 100 V165 H0z" fill="#8cc84b" role="img" aria-label="Green hills with houses for each district"/>
    <path d="M0 135 Q100 120 291 140 V165 H0z" fill="#6cb33f"/>
    <rect x="14" y="95" width="30" height="35" fill="#3e2c25"/><rect x="64" y="115" width="22" height="20" fill="#6cb33f"/>
    <rect x="112" y="88" width="32" height="32" fill="#6cb33f"/><rect x="180" y="85" width="32" height="32" fill="#3e2c25"/>
    <rect x="237" y="90" width="26" height="25" fill="#8cc84b"/>
    <g font-size="10" font-weight="300" fill="#fff"><text x="17" y="120">47%</text><text x="115" y="112">28%</text><text x="183" y="109">17%</text></g>
    <text x="67" y="128" font-size="7" fill="#fff" font-weight="300">9%</text><text x="241" y="108" font-size="8" fill="#fff" font-weight="300">11%</text>
    <g font-size="3.8" font-weight="700">
      <text x="12" y="70" fill="#333">Central City</text><text x="60" y="88" fill="#6cb33f">Downtown</text>
      <text x="112" y="62" fill="#6cb33f">Hills</text><text x="182" y="58" fill="#333">China Town</text><text x="240" y="70" fill="#6cb33f">Village</text>
    </g>
    <text x="12" y="75" class="tiny">Call a lender and request</text><text x="60" y="93" class="tiny">Call a lender and</text>
    <text x="112" y="67" class="tiny">Call a lender and</text><text x="182" y="63" class="tiny">Call a lender and</text><text x="240" y="75" class="tiny">Call a lender and</text>
  </svg>
</section>

<!-- 7 Eviction -->
<section class="slide">
  <h2 class="slide-title">Eviction Infographic</h2>
  <svg class="art" viewBox="0 0 291 165">
    <text x="20" y="58" font-size="4" fill="#333" font-weight="600">Workers</text>
    <text x="20" y="64" class="tiny">For every 6 emails received, we get 3</text>
    <text x="20" y="68" class="tiny">Phone calls. Suitable for all categories</text>
    <text x="20" y="72" class="tiny">business and personal presentation.</text>
    <text x="20" y="76" class="tiny">Feel free to write it this is yours.</text>
    <rect x="30" y="80" width="261" height="62" fill="#dcdcdc" role="img" aria-label="Bulldozer pushing toppled apartment buildings"/>
    <text x="170" y="78" font-size="4" fill="#6cb33f">Description</text><text x="240" y="82" font-size="4" fill="#3e2c25">Description</text>
    <rect x="0" y="142" width="291" height="23" fill="#5a4037"/>
  </svg>
</section>

<!-- 8 Urban Growth -->
<section class="slide">
  <h2 class="slide-title">Urban Growth</h2>
  <svg class="art" viewBox="0 0 291 165">
    <g font-size="7" font-weight="300" text-anchor="middle">
      <text x="34" y="72" fill="#444">0.1%</text><text x="94" y="72" fill="#6cb33f">1.5%</text>
      <text x="148" y="55" fill="#6cb33f">8%</text><text x="204" y="42" fill="#6cb33f">15%</text><text x="258" y="42" fill="#6cb33f">20%</text>
    </g>
    <g class="tiny" text-anchor="middle"><text x="34" y="76">Increase</text><text x="94" y="76">Increase</text><text x="148" y="59">Increase</text><text x="204" y="46">Increase</text><text x="258" y="46">Increase</text></g>
    <rect x="27" y="112" width="14" height="18" fill="#3e2c25"/>
    <rect x="80" y="110" width="10" height="20" fill="#6cb33f"/><rect x="91" y="104" width="14" height="26" fill="#3e2c25"/>
    <rect x="132" y="96" width="10" height="34" fill="#6cb33f"/><rect x="143" y="82" width="14" height="48" fill="#5aa532"/><rect x="158" y="100" width="8" height="30" fill="#3e2c25"/>
    <rect x="186" y="90" width="12" height="40" fill="#6cb33f"/><rect x="199" y="66" width="14" height="64" fill="#5aa532"/><rect x="214" y="86" width="10" height="44" fill="#6cb33f"/>
    <rect x="240" y="100" width="10" height="30" fill="#3e2c25"/><rect x="251" y="70" width="14" height="60" fill="#6cb33f"/><rect x="266" y="90" width="12" height="40" fill="#5aa532"/>
    <rect x="0" y="130" width="291" height="35" fill="#3e2c25"/>
    <g text-anchor="middle">
      <g class="lbl-w"><text x="34" y="139">2005</text><text x="94" y="139">2008</text><text x="148" y="139">2011</text><text x="204" y="139">2014</text><text x="258" y="139">2017</text></g>
      <g class="tiny-w"><text x="34" y="145">For every 6 emails</text><text x="94" y="145">For every 6 emails</text><text x="148" y="145">For every 6 emails</text><text x="204" y="145">For every 6 emails</text><text x="258" y="145">For every 6 emails</text>
      <text x="34" y="149">received, 3 calls</text><text x="94" y="149">received, 3 calls</text><text x="148" y="149">received, 3 calls</text><text x="204" y="149">received, 3 calls</text><text x="258" y="149">received, 3 calls</text></g>
    </g>
  </svg>
</section>

<!-- 9 Sales comparison -->
<section class="slide">
  <h2 class="slide-title caps">Sales Comparison</h2>
  <svg class="art" viewBox="0 0 291 165">
    <text x="50" y="60" font-size="3.8" fill="#333">2017 Sales</text><text x="228" y="60" font-size="3.8" fill="#6cb33f">2018 Sales</text>
    <line x1="145" y1="55" x2="145" y2="140" stroke="#ccc" stroke-width=".5" stroke-dasharray="2 2"/>
    <rect x="25" y="82" width="7" height="40" fill="#3e2c25"/><rect x="48" y="96" width="7" height="26" fill="#3e2c25"/>
    <rect x="71" y="88" width="7" height="34" fill="#3e2c25"/><rect x="94" y="78" width="7" height="44" fill="#3e2c25"/>
    <rect x="190" y="80" width="7" height="42" fill="#6cb33f"/><rect x="213" y="92" width="7" height="30" fill="#6cb33f"/>
    <rect x="236" y="86" width="7" height="36" fill="#6cb33f"/><rect x="259" y="78" width="7" height="44" fill="#6cb33f"/>
    <ellipse cx="145" cy="97" rx="14" ry="8" fill="#6cb33f"/><text x="145" y="99" font-size="5" fill="#fff" text-anchor="middle">VS</text>
    <text x="22" y="143" font-size="12" class="num">45%</text><text x="52" y="137" class="tiny">Lorem ipsum dolor</text><text x="52" y="141" class="tiny">sit amet consectetur</text>
    <text x="188" y="143" font-size="12" fill="#6cb33f" font-weight="300">68%</text><text x="218" y="137" class="tiny">Lorem ipsum dolor</text><text x="218" y="141" class="tiny">sit amet consectetur</text>
    <circle cx="8" cy="157" r="2" fill="#6cb33f"/><text x="12" y="159" font-size="5" class="brand">Venora</text>
  </svg>
</section>

<!-- 10 Title goes here -->
<section class="slide">
  <svg class="art" viewBox="0 0 291 165">
    <rect width="291" height="75" fill="#8a8a8a" role="img" aria-label="Faded architectural photograph"/>
    <text x="145" y="33" font-size="11" fill="#fff" font-weight="300" text-anchor="middle">YOUR TITLE GOES HERE</text>
    <rect x="0" y="75" width="97" height="90" fill="#5a4037"/><rect x="97" y="75" width="97" height="90" fill="#6cb33f"/><rect x="194" y="75" width="97" height="90" fill="#8cc84b"/>
    <g class="tiny-w">
      <text x="8" y="90">Lorem ipsum dolor sit amet,</text><text x="8" y="94">consectetur adipiscing elit, sed</text><text x="8" y="98">do eiusmod tempor incididunt</text><text x="8" y="102">ut labore et dolore magna.</text><text x="8" y="106">Ut enim ad minim veniam.</text>
      <text x="105" y="90">Lorem ipsum dolor sit amet,</text><text x="105" y="94">consectetur adipiscing elit, sed</text><text x="105" y="98">do eiusmod tempor incididunt</text><text x="105" y="102">ut labore et dolore magna.</text><text x="105" y="106">Ut enim ad minim veniam.</text>
      <text x="202" y="90">Lorem ipsum dolor sit amet,</text><text x="202" y="94">consectetur adipiscing elit, sed</text><text x="202" y="98">do eiusmod tempor incididunt</text><text x="202" y="102">ut labore et dolore magna.</text><text x="202" y="106">Ut enim ad minim veniam.</text>
    </g>
  </svg>
</section>

<!-- 11 Timeline page -->
<section class="slide">
  <svg class="art" viewBox="0 0 291 165">
    <rect width="291" height="72" fill="#3e2c25"/>
    <circle cx="122" cy="24" r="4" fill="#6cb33f"/><text x="129" y="28" font-size="11" fill="#fff" font-weight="700">Venora</text>
    <text x="145" y="56" font-size="10" fill="#fff" font-weight="300" text-anchor="middle">THIS IS YOUR TIMELINE PAGE</text>
    <text x="145" y="85" font-size="4" fill="#333" text-anchor="middle">Your Heading Here</text>
    <g class="tiny" text-anchor="middle"><text x="145" y="90">Lorem ipsum dolor sit amet, consectetur adipiscing</text><text x="145" y="94">elit, sed do eiusmod tempor incididunt ut labore</text><text x="145" y="98">et dolore magna aliqua ut enim ad minim</text></g>
    <line x1="145" y1="104" x2="145" y2="165" stroke="#ccc" stroke-width=".6"/>
    <circle cx="145" cy="134" r="8" fill="#6cb33f"/><circle cx="145" cy="134" r="3" fill="#fff"/>
  </svg>
</section>

<!-- 12 Your title -->
<section class="slide">
  <h2 class="slide-title caps">Your Title</h2>
  <svg class="art" viewBox="0 0 291 165">
    <rect x="145" y="0" width="146" height="82" fill="#7a8f9a" role="img" aria-label="Photograph of a palace courtyard with reflecting pool"/>
    <rect x="19" y="42" width="5" height="5" fill="none" stroke="#777" stroke-width=".6" transform="rotate(45 21.5 44.5)"/>
    <text x="30" y="46" font-size="4" fill="#444">Bullet point</text>
    <text x="30" y="51" class="tiny">Lorem ipsum dolor sit amet consectetur</text><text x="30" y="55" class="tiny">adipiscing elit sed do eiusmod tempor</text>
    <rect x="0" y="82" width="145" height="83" fill="#6cb33f"/>
    <g class="tiny-w"><text x="9" y="98">Lorem ipsum dolor sit amet, consectetur adipiscing elit,</text><text x="9" y="102">sed do eiusmod tempor incididunt ut labore et dolore</text><text x="9" y="106">magna aliqua. Ut enim ad minim veniam, quis nostrud</text><text x="9" y="110">exercitation ullamco laboris nisi ut aliquip ex ea.</text><text x="9" y="118">Duis aute irure dolor in reprehenderit in voluptate</text><text x="9" y="122">velit esse cillum dolore eu fugiat nulla pariatur.</text></g>
    <rect x="162" y="104" width="6" height="5" fill="#8cc84b"/>
    <text x="172" y="109" font-size="4" fill="#6cb33f">Bullet point</text>
    <text x="172" y="114" class="tiny">Lorem ipsum dolor sit amet consectetur</text><text x="172" y="118" class="tiny">adipiscing elit sed do eiusmod tempor</text>
  </svg>
</section>

<!-- 13 Your title 2 -->
<section class="slide">
  <h2 class="slide-title caps">Your Title</h2>
  <svg class="art" viewBox="0 0 291 165">
    <rect x="146" y="0" width="145" height="88" fill="#a5664a" role="img" aria-label="Photograph of colourful canal houses reflected in water"/>
    <rect x="146" y="88" width="145" height="77" fill="#3e2c25"/>
    <g class="tiny-w"><text x="154" y="100">Lorem ipsum dolor sit amet, consectetur adipiscing elit,</text><text x="154" y="104">sed do eiusmod tempor incididunt ut labore et dolore</text><text x="154" y="108">magna aliqua. Ut enim ad minim veniam, quis nostrud</text><text x="154" y="112">exercitation ullamco laboris nisi ut aliquip ex ea.</text><text x="154" y="120">Duis aute irure dolor in reprehenderit in voluptate</text><text x="154" y="124">velit esse cillum dolore eu fugiat nulla pariatur.</text></g>
    <rect x="19" y="45" width="5" height="5" fill="none" stroke="#777" stroke-width=".6" transform="rotate(45 21.5 47.5)"/>
    <text x="30" y="49" font-size="4" fill="#444">Bullet Point</text>
    <text x="30" y="54" class="tiny">Lorem ipsum dolor sit amet, consectetur</text><text x="30" y="58" class="tiny">adipiscing elit sed do eiusmod tempor</text>
    <rect x="18" y="79" width="6" height="5" fill="#8cc84b"/>
    <text x="30" y="84" font-size="4" fill="#6cb33f">Chart</text>
    <text x="30" y="89" class="tiny">Lorem ipsum dolor sit amet, consectetur</text><text x="30" y="93" class="tiny">adipiscing elit sed do eiusmod tempor</text>
    <g fill="#8cc84b"><circle cx="19" cy="118" r="1.3"/><circle cx="24" cy="115" r="1.3"/><circle cx="24" cy="121" r="1.3"/></g>
    <path d="M19 118L24 115M19 118L24 121" stroke="#8cc84b" stroke-width=".5"/>
    <text x="30" y="120" font-size="4" fill="#6cb33f">Share</text>
    <text x="30" y="125" class="tiny">Lorem ipsum dolor sit amet, consectetur</text><text x="30" y="129" class="tiny">adipiscing elit sed do eiusmod tempor</text>
  </svg>
</section>

<!-- 14 Timeline middle -->
<section class="slide">
  <svg class="art" viewBox="0 0 291 165">
    <line x1="145" y1="0" x2="145" y2="165" stroke="#ccc" stroke-width=".6"/>
    <g fill="#6cb33f"><circle cx="145" cy="22" r="6"/><circle cx="145" cy="49" r="6"/><circle cx="145" cy="107" r="6"/></g>
    <g fill="#fff"><circle cx="145" cy="22" r="2"/><circle cx="145" cy="49" r="2"/><circle cx="145" cy="107" r="2"/></g>
    <text x="132" y="21" font-size="3.2" fill="#6cb33f" text-anchor="end">YOUR TITLE</text>
    <g class="tiny" text-anchor="end"><text x="132" y="26">Duis aute irure dolor in reprehenderit in voluptate velit</text><text x="132" y="30">esse cillum dolore eu fugiat nulla pariatur.</text></g>
    <text x="160" y="50" font-size="3.2" fill="#6cb33f">YOUR TITLE</text>
    <text x="160" y="64" font-size="10" class="num">85%</text>
    <text x="160" y="71" class="tiny">Duis aute irure dolor in reprehenderit</text><text x="160" y="75" class="tiny">in voluptate velit esse cillum dolore</text>
    <text x="132" y="106" font-size="3.2" fill="#6cb33f" text-anchor="end">YOUR TITLE</text>
    <rect x="30" y="115" width="100" height="30" fill="#3e2c25"/>
    <g class="tiny-w" text-anchor="middle"><text x="70" y="124">Duis aute irure dolor in</text><text x="70" y="128">reprehenderit in voluptate</text><text x="70" y="132">velit esse cillum dolore</text></g>
    <rect x="110" y="122" width="11" height="14" fill="none" stroke="#fff" stroke-width=".6"/>
  </svg>
</section>

<!-- 15 Who we are -->
<section class="slide">
  <h2 class="slide-title caps">Who We Are?</h2>
  <svg class="art" viewBox="0 0 291 165">
    <g font-size="6" font-weight="300">
      <text x="20" y="48" fill="#333">A Title About</text><text x="20" y="55" fill="#333">Contents</text>
      <text x="20" y="86" fill="#6cb33f">A Title About</text><text x="20" y="93" fill="#6cb33f">Contents</text>
      <text x="20" y="124" fill="#6cb33f">A Title About</text><text x="20" y="131" fill="#6cb33f">Contents</text>
    </g>
    <g class="tiny"><text x="20" y="59">Lorem ipsum dolor sit</text><text x="20" y="97">Lorem ipsum dolor sit</text><text x="20" y="135">Lorem ipsum dolor sit</text>
      <text x="90" y="43">2015</text><text x="90" y="81">2017</text><text x="90" y="119">2018</text></g>
    <g stroke-width=".6"><line x1="100" y1="43" x2="276" y2="43" stroke="#3e2c25"/><line x1="100" y1="81" x2="276" y2="81" stroke="#6cb33f"/><line x1="100" y1="119" x2="276" y2="119" stroke="#6cb33f"/></g>
    <g class="tiny">
      <text x="90" y="50">Lorem ipsum dolor sit amet, consectetur adipiscing elit, sed do eiusmod tempor</text><text x="90" y="54">incididunt ut labore et dolore magna aliqua. Ut enim ad minim veniam quis</text><text x="90" y="58">nostrud exercitation ullamco laboris nisi ut aliquip ex ea commodo.</text>
      <text x="90" y="88">Lorem ipsum dolor sit amet, consectetur adipiscing elit, sed do eiusmod tempor</text><text x="90" y="92">incididunt ut labore et dolore magna aliqua. Ut enim ad minim veniam quis</text><text x="90" y="96">nostrud exercitation ullamco laboris nisi ut aliquip ex ea commodo.</text>
      <text x="90" y="126">Lorem ipsum dolor sit amet, consectetur adipiscing elit, sed do eiusmod tempor</text><text x="90" y="130">incididunt ut labore et dolore magna aliqua. Ut enim ad minim veniam quis</text><text x="90" y="134">nostrud exercitation ullamco laboris nisi ut aliquip ex ea commodo.</text>
    </g>
    <circle cx="8" cy="157" r="2" fill="#6cb33f"/><text x="12" y="159" font-size="5" class="brand">Venora</text>
  </svg>
</section>

<!-- 16 Three steps -->
<section class="slide">
  <h2 class="slide-title caps">Three Steps</h2>
  <svg class="art" viewBox="0 0 291 165">
    <circle cx="27" cy="58" r="5" fill="#3e2c25"/><circle cx="27" cy="88" r="5" fill="#8cc84b"/><circle cx="27" cy="117" r="5" fill="#3e2c25"/>
    <g font-size="4" fill="#444"><text x="38" y="59">Sample Text</text><text x="38" y="89" fill="#6cb33f">Sample Text</text><text x="38" y="118" fill="#6cb33f">Sample Text</text></g>
    <g class="tiny"><text x="38" y="64">Lorem ipsum dolor sit amet, consectetur adipiscing elit. Duis</text><text x="38" y="68">ligula lorem, consequat eget, tristique nec, auctor quis, purus.</text>
      <text x="38" y="94">Lorem ipsum dolor sit amet, consectetur adipiscing elit. Duis</text><text x="38" y="98">ligula lorem, consequat eget, tristique nec, auctor quis, purus.</text>
      <text x="38" y="123">Lorem ipsum dolor sit amet, consectetur adipiscing elit. Duis</text><text x="38" y="127">ligula lorem, consequat eget, tristique nec, auctor quis, purus.</text></g>
    <g fill="none" stroke-width="11">
      <circle cx="243" cy="42" r="23" stroke="#3e2c25"/>
      <circle cx="213" cy="90" r="23" stroke="#8cc84b"/>
      <circle cx="243" cy="132" r="23" stroke="#6cb33f"/>
    </g>
    <g fill="#fff"><circle cx="243" cy="42" r="7"/><circle cx="213" cy="90" r="7" fill="#8cc84b"/><circle cx="243" cy="132" r="7"/></g>
    <circle cx="8" cy="157" r="2" fill="#6cb33f"/><text x="12" y="159" font-size="5" class="brand">Venora</text>
  </svg>
</section>

<!-- 17 Timeline end -->
<section class="slide">
  <svg class="art" viewBox="0 0 291 165">
    <line x1="145" y1="0" x2="145" y2="98" stroke="#ccc" stroke-width=".6"/>
    <g fill="#6cb33f"><circle cx="145" cy="30" r="6"/><circle cx="145" cy="98" r="6"/></g>
    <g fill="#fff"><circle cx="145" cy="30" r="2"/><circle cx="145" cy="98" r="2"/></g>
    <text x="158" y="26" font-size="7" font-weight="800" fill="#333">YOUR</text><text x="158" y="35" font-size="7" font-weight="800" fill="#333">TITLE HERE</text>
    <text x="133" y="55" font-size="4" font-weight="700" fill="#333" text-anchor="end">TIMELINE</text><text x="133" y="60" font-size="4" font-weight="700" fill="#333" text-anchor="end">FINISH</text>
    <text x="133" y="75" font-size="10" fill="#6cb33f" font-weight="300" text-anchor="end">85%</text>
    <g class="tiny" text-anchor="end"><text x="110" y="66">Duis aute irure dolor in</text><text x="110" y="70">reprehenderit in voluptate</text></g>
    <text x="158" y="56" class="tiny">Duis aute irure dolor in reprehenderit in voluptate velit esse</text><text x="158" y="60" class="tiny">cillum dolore eu fugiat nulla pariatur excepteur.</text>
    <text x="158" y="96" font-size="3.2" fill="#333">YOUR TITLE</text>
    <text x="158" y="100" class="tiny">Duis aute irure dolor in reprehenderit in voluptate velit esse</text>
    <circle cx="122" cy="138" r="4" fill="#6cb33f"/><text x="129" y="142" font-size="11" class="brand">Venora</text>
  </svg>
</section>

<!-- 18 Project timeline -->
<section class="slide">
  <h2 class="slide-title caps">Project Timeline</h2>
  <svg class="art" viewBox="0 0 291 165">
    <g class="tiny" text-anchor="middle">
      <text x="52" y="46">Project step</text><text x="88" y="46">Jan</text><text x="103" y="46">Feb</text><text x="118" y="46">Mar</text><text x="133" y="46">Apr</text><text x="148" y="46">May</text><text x="163" y="46">June</text><text x="178" y="46">July</text><text x="193" y="46">Aug</text><text x="208" y="46">Sep</text><text x="223" y="46">Oct</text><text x="238" y="46">Nov</text><text x="253" y="46">Dec</text>
    </g>
    <g stroke="#ddd" stroke-width=".4">
      <line x1="25" y1="49" x2="265" y2="49"/><line x1="25" y1="58" x2="265" y2="58"/><line x1="25" y1="67" x2="265" y2="67"/><line x1="25" y1="76" x2="265" y2="76"/><line x1="25" y1="85" x2="265" y2="85"/><line x1="25" y1="94" x2="265" y2="94"/><line x1="25" y1="103" x2="265" y2="103"/><line x1="25" y1="112" x2="265" y2="112"/><line x1="25" y1="121" x2="265" y2="121"/><line x1="25" y1="130" x2="265" y2="130"/>
      <line x1="80" y1="42" x2="80" y2="130"/>
    </g>
    <g class="tiny"><text x="40" y="55">Process 01</text><text x="40" y="64">Process 02</text><text x="40" y="73">Process 03</text><text x="40" y="82">Process 04</text><text x="40" y="91">Process 05</text><text x="40" y="100">Process 06</text><text x="40" y="109">Process 07</text><text x="40" y="118">Process 08</text><text x="40" y="127">Process 09</text></g>
    <g>
      <rect x="84" y="52" width="28" height="3.5" rx="1.7" fill="#3e2c25"/><rect x="228" y="52" width="25" height="3.5" rx="1.7" fill="#3e2c25"/>
      <rect x="92" y="61" width="16" height="3.5" rx="1.7" fill="#aaa"/><rect x="150" y="61" width="24" height="3.5" rx="1.7" fill="#6cb33f"/>
      <rect x="110" y="70" width="100" height="3.5" rx="1.7" fill="#6cb33f"/>
      <rect x="138" y="79" width="32" height="3.5" rx="1.7" fill="#3e2c25"/><rect x="196" y="79" width="22" height="3.5" rx="1.7" fill="#8cc84b"/>
      <rect x="180" y="88" width="78" height="3.5" rx="1.7" fill="#3e2c25"/>
      <rect x="128" y="97" width="18" height="3.5" rx="1.7" fill="#8cc84b"/>
      <rect x="148" y="106" width="32" height="3.5" rx="1.7" fill="#3e2c25"/>
      <rect x="180" y="115" width="26" height="3.5" rx="1.7" fill="#6cb33f"/>
      <rect x="220" y="124" width="34" height="3.5" rx="1.7" fill="#8cc84b"/>
    </g>
    <g class="tiny"><circle cx="58" cy="139" r="1.2" fill="#3e2c25"/><text x="61" y="140">Description</text><circle cx="95" cy="139" r="1.2" fill="#6cb33f"/><text x="98" y="140">Description</text><circle cx="132" cy="139" r="1.2" fill="#3e2c25"/><text x="135" y="140">Description</text><circle cx="169" cy="139" r="1.2" fill="#8cc84b"/><text x="172" y="140">Description</text><circle cx="206" cy="139" r="1.2" fill="#3e2c25"/><text x="209" y="140">Description</text></g>
    <circle cx="8" cy="157" r="2" fill="#6cb33f"/><text x="12" y="159" font-size="5" class="brand">Venora</text>
  </svg>
</section>

<!-- 19 Key points -->
<section class="slide">
  <svg class="art" viewBox="0 0 291 165">
    <rect x="0" y="0" width="146" height="165" fill="#6f8a5a" role="img" aria-label="Photograph of a stone manor house behind a lawn"/>
    <rect x="146" y="0" width="145" height="165" fill="#5a4037"/>
    <text x="164" y="30" font-size="11" fill="#fff" font-weight="300">KEY POINTS</text>
    <line x1="164" y1="35" x2="180" y2="35" stroke="#fff" stroke-width="1"/>
    <g font-size="4.6" fill="#fff" font-weight="300">
      <text x="172" y="58">Lorem ipsum dolor sit amet.</text><text x="172" y="71">consectetur adipiscing elit, sed do</text><text x="172" y="84">eiusmod tempor incididunt ut</text><text x="172" y="97">labore et dolore magna aliqua. Ut</text><text x="172" y="110">enim ad minim veniam, quis nostrud</text><text x="172" y="123">exercitation ullamco laboris nisi ut</text><text x="172" y="136">aliquip ex ea commodo consequat</text>
    </g>
    <g fill="#fff"><circle cx="167" cy="57" r=".9"/><circle cx="167" cy="70" r=".9"/><circle cx="167" cy="83" r=".9"/><circle cx="167" cy="96" r=".9"/><circle cx="167" cy="109" r=".9"/><circle cx="167" cy="122" r=".9"/><circle cx="167" cy="135" r=".9"/></g>
  </svg>
</section>

<!-- 20 Three bullets -->
<section class="slide">
  <h2 class="slide-title caps">Three Bullets Area</h2>
  <svg class="art" viewBox="0 0 291 165">
    <rect x="0" y="34" width="291" height="82" fill="#3f3a3e" role="img" aria-label="Photograph of a row of modern townhouses at dusk"/>
    <circle cx="54" cy="109" r="14" fill="#3e2c25"/><circle cx="145" cy="103" r="14" fill="#6cb33f"/><circle cx="240" cy="109" r="14" fill="#3e2c25"/>
    <g fill="#fff"><circle cx="50" cy="109" r="2"/><circle cx="58" cy="104" r="2"/><circle cx="58" cy="114" r="2"/></g>
    <path d="M50 109L58 104M50 109L58 114" stroke="#fff" stroke-width="1"/>
    <path d="M137 101l8-4 8 4-8 4zM137 105l8 4 8-4" fill="none" stroke="#fff" stroke-width="1.2"/>
    <path d="M234 115h12l-2-8-4-4-4 4z" fill="#fff"/>
    <g class="tiny" text-anchor="middle">
      <text x="54" y="131">Lorem ipsum dolor sit amet</text><text x="54" y="135">consectetur adipiscing elit sed</text><text x="54" y="139">do eiusmod tempor incididunt</text>
      <text x="145" y="131">Lorem ipsum dolor sit amet</text><text x="145" y="135">consectetur adipiscing elit sed</text><text x="145" y="139">do eiusmod tempor incididunt</text>
      <text x="240" y="131">Lorem ipsum dolor sit amet</text><text x="240" y="135">consectetur adipiscing elit sed</text><text x="240" y="139">do eiusmod tempor incididunt</text>
    </g>
    <circle cx="8" cy="157" r="2" fill="#6cb33f"/><text x="12" y="159" font-size="5" class="brand">Venora</text>
  </svg>
</section>

<!-- 21 Thank you -->
<section class="slide">
  <svg class="art" viewBox="0 0 291 165">
    <defs><linearGradient id="thanks-bg" x1="0" y1="0" x2="1" y2="1"><stop offset="0" stop-color="#7dbb45"/><stop offset="1" stop-color="#4f9a2c"/></linearGradient></defs>
    <rect width="291" height="165" fill="url(#thanks-bg)" role="img" aria-label="Green tinted photograph of a residential building"/>
    <path d="M291 95 L291 165 L200 165z" fill="#fff"/>
    <text x="14" y="55" font-size="18" font-weight="800" fill="#fff">THANK YOU</text>
    <text x="14" y="69" font-size="9" font-weight="300" fill="#fff">SEND YOUR FEEDBACK</text>
    <g fill="#fff"><circle cx="18" cy="99" r="1.5"/><circle cx="18" cy="107" r="1.5"/><circle cx="18" cy="115" r="1.5"/><circle cx="18" cy="123" r="1.5"/></g>
    <g class="tiny-w"><text x="24" y="98">45 Alameda Sur</text><text x="24" y="101">Lima, Peru</text><text x="24" y="108">+51 1 555 0142</text><text x="24" y="116">contacto@venora-grupo.pe</text><text x="24" y="124">www.venora-grupo.pe</text></g>
    <circle cx="247" cy="146" r="3.5" fill="#6cb33f"/><text x="253" y="150" font-size="10" class="brand">Venora</text>
  </svg>
</section>

</main>
</body>
</html>
```